RW Frameworks Inc Business cards

We need business cards using our existing logo but slightly modified. Right now the logo says RW Framework Masonry. We want to keep the RW part of the design, but replace the Framework Masonry portion with "FRAMEWORKS". Please see the attached file.
Ideally this would be a blank template so we can add Different Names, titles, and phone numbers later.
On the one side we want only the logo and on the other side the detail. I'm attaching an example for you to see.
Please reach out with any other questions. Our address and other details will be given out once we find a design we like.

Target Market(s)

Construction Industry

```html
<!DOCTYPE html>
<html lang="en">
<head>
<meta charset="utf-8">
<title>RW Frameworks Inc – Business Card</title>
<link rel="stylesheet" href="https://fonts.googleapis.com/css2?family=Raleway:wght@400;500;700;800&display=swap">
<style>
  :root {
    --brand-blue: #0077c8;
    --ink-grey: #3f3f44;
    --card-white: #f7f7f7;
    --backdrop: #e4e4e6;
  }
  * { box-sizing: border-box; margin: 0; padding: 0; }
  html, body {
    width: 1200px; height: 900px; overflow: hidden;
    background: var(--backdrop);
    font-family: "Raleway", sans-serif;
  }
  .sheet {
    width: 1200px; height: 900px;
    display: flex; flex-direction: column;
    align-items: center; justify-content: center; gap: 50px;
  }
  .card {
    width: 665px; height: 380px;
    position: relative;
    box-shadow: 0 6px 18px rgba(0,0,0,.12);
  }

  /* Logo side */
  .card--back {
    background: var(--brand-blue);
    display: flex; align-items: center; justify-content: center;
  }
  .wordmark {
    display: flex; flex-direction: column; align-items: center;
    font-weight: 700; line-height: 1;
  }
  .wordmark__initials { font-size: 118px; letter-spacing: 2px; }
  .wordmark__name { font-size: 22px; letter-spacing: 17px; margin-top: 12px; padding-left: 17px; }
  .card--back .wordmark { color: #ffffff; }

  /* Detail side */
  .card--front {
    background: var(--card-white);
  }
  .card--front .wordmark {
    position: absolute; left: 70px; top: 130px; width: 225px;
    color: var(--brand-blue);
  }
  .card--front .wordmark__initials { font-size: 92px; }
  .card--front .wordmark__name { font-size: 17px; letter-spacing: 10px; margin-top: 10px; padding-left: 10px; }

  .divider {
    position: absolute; left: 333px; top: 103px;
    width: 2px; height: 172px; background: var(--brand-blue);
  }
  .details {
    position: absolute; left: 365px; top: 100px;
    color: var(--ink-grey);
  }
  .details__name {
    font-weight: 800; font-size: 25px; color: var(--brand-blue);
    letter-spacing: .3px; line-height: 1;
  }
  .details__title { font-size: 15px; font-weight: 500; margin-top: 9px; }
  .details__rule { width: 17px; height: 2px; background: var(--brand-blue); margin: 8px 0 10px; }
  .details__address { font-size: 15px; line-height: 19px; font-weight: 500; }
  .contact { list-style: none; margin-top: 6px; }
  .contact li {
    display: flex; align-items: center; gap: 11px;
    font-size: 15px; font-weight: 500; height: 25px;
  }
  .contact svg { width: 15px; height: 15px; fill: var(--brand-blue); flex: none; }
</style>
</head>
<body>
<main class="sheet">
  <section class="card card--back" aria-label="Logo side">
    <div class="wordmark">
      <span class="wordmark__initials">RW</span>
      <span class="wordmark__name">FRAMEWORKS</span>
    </div>
  </section>

  <section class="card card--front" aria-label="Detail side">
    <div class="wordmark">
      <span class="wordmark__initials">RW</span>
      <span class="wordmark__name">FRAMEWORKS</span>
    </div>
    <div class="divider"></div>
    <div class="details">
      <h1 class="details__name">DANIEL REYES</h1>
      <p class="details__title">FOUNDER</p>
      <div class="details__rule"></div>
      <p class="details__address">YOUR LOCATION STREET<br>HERE UNITED STREET-9100</p>
      <ul class="contact">
        <li>
          <svg viewBox="0 0 24 24" aria-hidden="true"><path d="M6.6 10.8a15.1 15.1 0 0 0 6.6 6.6l2.2-2.2a1 1 0 0 1 1-.25 11.4 11.4 0 0 0 3.6.57 1 1 0 0 1 1 1V20a1 1 0 0 1-1 1A17 17 0 0 1 3 4a1 1 0 0 1 1-1h3.5a1 1 0 0 1 1 1c0 1.25.2 2.45.57 3.6a1 1 0 0 1-.25 1z"/></svg>
          +000000000000
        </li>
        <li>
          <svg viewBox="0 0 24 24" aria-hidden="true"><path d="M2 5h20v14H2zm2 2v.4l8 5.3 8-5.3V7zm0 2.8V17h16V9.8l-8 5.3z"/></svg>
          INFO@YOURMAIL.COM
        </li>
        <li>
          <svg viewBox="0 0 24 24" aria-hidden="true"><path d="M12 2a10 10 0 1 0 0 20 10 10 0 0 0 0-20zm-1 17.9A8 8 0 0 1 4.1 10.9L9 15.8v1a2 2 0 0 0 2 2zm6.9-2.5A2 2 0 0 0 16 16h-1v-3a1 1 0 0 0-1-1H8v-2h2a1 1 0 0 0 1-1V7h2a2 2 0 0 0 2-2v-.4a8 8 0 0 1 2.9 12.8z"/></svg>
          WWW.YOURWEBSITE.COM
        </li>
      </ul>
    </div>
  </section>
</main>
</body>
</html>
```